Site Design - PSD Only - festival management

We are looking for a final design for our B2B marketplace. The project is a social commerce platform managing the application and transaction process for festivals and local events. The site design should be based on either Bootstrap or Plinth Framework. We will provide logos and example images.

Two of the most critical pages will be the home page and the search interface, as well several dashboards. Beyond that, most of the pages will be standard forms and other typical pages that drop into the general site theme. The design tends towards minimalism to simplify the UX and speed up the interface. It incorporates elements from the the following websites. Although the wireframes may lift design elements directly from some of these sites, we are looking for a design that incorporates them more as inspiration.

quilo.co - good example of minimalist structure on internal pages
ravtorn.com - some similarities on search pages, etc.
vexdal.com - nice simple layout for features on home and internal pages
mossbrackle.com - nice alternative to standard bootstrap template

We're nearing the end of this project.  I've received some good submissions , but they are all variations on the exact same theme.  I would still like to see something that doesn't look like a bootstrap template.  I suggested the following idea to a few of the submitters, but now I am adding it to the main project description in hopes of stoking the engine.

The idea I had is for something a little less "bootstrappy" riffs on the design at mossbrackle.com with a flat background color that nicely offsets the blue in the logo. Rather than pulling in a stock image I thought about creating a derivation of the iconic Harrowmere poster, perhaps with vendor tents as tuning pegs and a silhouette of people on the neck. Just throwing that out there. 

I'm not a designer, though, so here's hoping we can see some different ideas while the project is still open.

Thanks.

Target Market(s)

Target market: Festival and event organizers; event participants including exhibitors, vendors, musicians, authors, volunteers, etc.

Industry/Entity Type

Festival

Requirements
Must have
• Home page, Search page, User dash, Organization dash, Event dash, Features, FAQ, various forms
Nice to have
• Would like to see some alternative designs to the standard bootstrap templates...creativity is encouraged.
Should not have
• Should not look like it was pulled off of the shelf.

```html
<!DOCTYPE html>
<html lang="en">
<head>
<meta charset="utf-8">
<title>Tarnalo – Festival Management</title>
<link href="https://fonts.googleapis.com/css2?family=Ubuntu:wght@400;500;700&family=Arimo:wght@400;700&family=Bebas+Neue&display=swap" rel="stylesheet">
<style>
:root{
  --orange:#f2661c;
  --orange-soft:#f7a271;
  --yellow:#f5a814;
  --ink:#14202e;
  --text:#444;
  --muted:#888;
  --header-bg:#f1f1f1;
  --line:#d6d6d6;
  --menu-bg:#1c2a3c;
  --hero-deep:#0b1440;
  --hero-mid:#1f3fb0;
  --hero-light:#4b7be6;
  --footer-bg:#1d1d1d;
  --footer-base:#121212;
  --white:#fff;
  --logo-blue:#2a90c8;
}
*{box-sizing:border-box;margin:0;padding:0}
html,body{width:1200px;height:1054px;overflow:hidden;background:var(--white);font-family:"Arimo",Arial,sans-serif;color:var(--text)}
.page{position:relative;width:1200px;height:1054px}

/* header */
.site-header{position:absolute;left:0;top:0;width:1200px;height:101px;background:var(--header-bg);border-bottom:1px solid var(--line)}
.tab-mark{position:absolute;top:0;height:5px;background:#b8b8b8}
.tab-mark.is-active{background:var(--orange)}
.brand{position:absolute;left:217px;top:54px;display:flex;align-items:center;gap:6px;font-family:"Ubuntu",sans-serif;font-weight:500;font-size:19px;letter-spacing:1px;color:var(--ink)}
.brand-dot{width:20px;height:20px;border-radius:50%;background:var(--logo-blue)}
.action-divider{position:absolute;top:0;width:1px;height:101px;background:var(--line)}
.action{position:absolute;top:30px;width:60px;text-align:center;font-family:"Ubuntu",sans-serif;font-weight:500;font-size:16px;color:#666}
.action svg{display:block;margin:0 auto 3px}
.action.is-active{color:var(--orange)}
.tooltip{position:absolute;left:332px;top:89px;width:130px;height:15px;background:#e6e6e6;border:1px solid #ccc;border-radius:2px;font-size:9px;font-style:italic;color:#555;text-align:center;line-height:13px}
.search{position:absolute;left:759px;top:7px;width:167px;height:26px;background:var(--white);border:1px solid #ddd;font-size:9px;color:#333;padding:8px 8px 0}
.search svg{position:absolute;right:7px;top:6px}
.social-top{position:absolute;left:933px;top:5px;width:58px;height:26px;background:var(--white);border:1px solid #ddd;display:flex;gap:12px;padding:7px 0 0 10px}
.social-top span{width:12px;height:12px;background:#3b5a98}
.social-top span+span{background:#29a7e0}
.main-nav{position:absolute;top:64px;left:665px;display:flex;gap:13px;font-size:10px;font-weight:700;color:#444}
.main-nav .has-menu::after{content:"";display:inline-block;width:5px;height:5px;border-right:1.5px solid #444;border-bottom:1.5px solid #444;transform:rotate(45deg);margin:0 0 3px 5px}
.account{position:absolute;left:912px;top:64px;font-size:10px;color:var(--orange)}

/* dropdown */
.menu{position:absolute;background:var(--menu-bg);padding:0 8px;box-shadow:0 2px 4px rgba(0,0,0,.4);z-index:3}
.menu-item{font-size:9px;white-space:nowrap;color:var(--white);padding:8px 0 7px;border-bottom:1px solid #3b4a5d}
.menu-item:last-child{border-bottom:0}
.menu-item small{display:block;font-size:7.5px;font-style:italic;color:#9aa7b6;margin-top:1px}
.menu-item.is-hover{color:var(--orange)}
.menu-primary{left:663px;top:89px;width:127px;height:98px}
.menu-sub{left:791px;top:148px;width:122px;height:61px}

/* hero */
.hero{position:absolute;left:0;top:101px;width:1200px;height:288px}
.hero-photo{position:absolute;inset:0;background:radial-gradient(ellipse at 48% 12%,var(--hero-light) 0%,var(--hero-mid) 35%,var(--hero-deep) 75%),var(--hero-deep)}
.hero-crowd{position:absolute;left:0;bottom:0;width:1200px;height:120px;background:linear-gradient(to bottom,rgba(2,4,15,0),rgba(2,4,15,.9) 55%)}
.hero-title{position:absolute;left:0;width:1200px;top:70px;text-align:center;font-family:"Bebas Neue",sans-serif;font-size:72px;letter-spacing:2px;color:var(--white);line-height:1}
.hero-lead{position:absolute;left:0;width:1200px;top:141px;text-align:center;font-family:"Ubuntu",sans-serif;font-weight:500;font-size:16px;line-height:22px;color:var(--white)}
.cta{position:absolute;left:481px;top:201px;width:236px;height:38px;background:var(--yellow);border-radius:3px;border-bottom:3px solid #c9830a;font-family:"Ubuntu",sans-serif;font-weight:500;font-size:18px;color:var(--white);text-align:center;line-height:36px}

/* slider */
.slider-track{position:absolute;left:409px;top:390px;width:368px;height:2px;background:#ddd}
.slider-progress{position:absolute;left:409px;top:389px;width:33px;height:4px;background:var(--yellow)}
.slider-dot{position:absolute;top:385px;width:12px;height:12px;border-radius:50%;background:#c8c8c8;border:2px solid #e8e8e8}
.slider-dot.is-active{background:var(--yellow);border-color:#f7d07e}
.slider-arrow{position:absolute;top:374px;width:36px;height:36px;border-radius:50%;background:var(--white);border:1px solid #ddd;box-shadow:0 1px 3px rgba(0,0,0,.2)}
.slider-arrow svg{position:absolute;left:12px;top:11px}

/* features */
.feature{position:absolute;width:219px;height:180px;background:var(--white);border:1px solid #e2e2e2;box-shadow:0 1px 3px rgba(0,0,0,.12);text-align:center;padding-top:22px;overflow:hidden}
.feature svg{display:block;margin:0 auto}
.feature-title{font-family:"Ubuntu",sans-serif;font-weight:500;font-size:17px;line-height:18px;color:var(--ink);margin:12px 12px 12px}
.feature-text{font-size:10px;line-height:13px;color:#555;padding:0 22px}
.feature.is-hover{border-color:var(--orange-soft)}
.feature.is-hover .feature-title{color:var(--orange)}
.feature-more{position:absolute;left:0;width:100%;bottom:8px;font-size:8.5px;font-weight:700;color:var(--orange)}
.feature-corner{position:absolute;right:0;bottom:0;width:0;height:0;border-left:40px solid transparent;border-bottom:40px solid var(--orange-soft)}

/* footer */
.site-footer{position:absolute;left:0;top:947px;width:1200px;height:64px;background:var(--footer-bg)}
.footer-nav{position:absolute;left:215px;top:30px;display:flex;gap:14px;font-size:10px;color:var(--white)}
.footer-nav span+span::before{content:"";display:inline-block;width:4px;height:4px;background:#666;border-radius:50%;margin:0 14px 2px 0}
.footer-social{position:absolute;left:624px;top:28px;display:flex;gap:14px;font-size:8.5px;font-weight:700}
.footer-social span{display:flex;align-items:center;gap:4px;color:#39a9e0}
.footer-social span:first-child{color:var(--orange)}
.footer-social i{display:block;width:14px;height:14px;background:#3b5a98}
.footer-social span:first-child i{background:var(--orange)}
.footer-social span:nth-child(3) i{background:#29a7e0}
.footer-social span:nth-child(4) i{background:#1c6ea4}
.footer-brand{position:absolute;left:903px;top:27px;display:flex;align-items:center;gap:5px;font-family:"Ubuntu",sans-serif;font-weight:500;font-size:16px;color:#777}
.footer-brand i{width:14px;height:14px;border-radius:50%;background:#555}
.footer-base{position:absolute;left:0;top:1011px;width:1200px;height:43px;background:var(--footer-base);font-size:10px;color:var(--white)}
.copyright{position:absolute;left:215px;top:18px;color:#666;font-size:9px}
.footer-links{position:absolute;right:217px;top:18px;display:flex;gap:30px}
</style>
</head>
<body>
<div class="page">

  <header class="site-header">
    <div class="tab-mark is-active" style="left:367px;width:61px"></div>
    <div class="tab-mark" style="left:442px;width:48px"></div>
    <div class="tab-mark" style="left:504px;width:48px"></div>

    <div class="brand"><span class="brand-dot"></span>TARNALO</div>

    <div class="action-divider" style="left:434px"></div>
    <div class="action-divider" style="left:498px"></div>

    <div class="action is-active" style="left:366px">
      <svg width="20" height="24" viewBox="0 0 20 24"><path d="M10 1a8 8 0 0 0-8 8c0 6 8 14 8 14s8-8 8-14a8 8 0 0 0-8-8z" fill="none" stroke="#f2661c" stroke-width="2.4"/><circle cx="10" cy="9" r="3" fill="#f2661c"/></svg>
      Apply
    </div>
    <div class="action" style="left:435px">
      <svg width="24" height="24" viewBox="0 0 24 24"><rect x="2" y="4" width="20" height="18" rx="2" fill="none" stroke="#888" stroke-width="2"/><line x1="2" y1="9" x2="22" y2="9" stroke="#888" stroke-width="2"/><line x1="7" y1="1" x2="7" y2="6" stroke="#888" stroke-width="2"/><line x1="17" y1="1" x2="17" y2="6" stroke="#888" stroke-width="2"/><path d="M12 12v7M8.5 15.5h7" stroke="#888" stroke-width="2"/></svg>
      Add
    </div>
    <div class="action" style="left:497px">
      <svg width="28" height="24" viewBox="0 0 28 24"><circle cx="11" cy="6" r="5" fill="#999"/><path d="M1 23c0-7 4-10 10-10s10 3 10 10z" fill="#999"/><circle cx="20" cy="7" r="4" fill="#bbb"/><path d="M16 13c7-1 11 2 11 9h-4" fill="#bbb"/></svg>
      Join
    </div>
    <div class="tooltip">To a festival or a local event.</div>

    <div class="search">Find your information here...
      <svg width="13" height="13" viewBox="0 0 13 13"><circle cx="5.5" cy="5.5" r="4" fill="none" stroke="#f2661c" stroke-width="2"/><line x1="8.5" y1="8.5" x2="12" y2="12" stroke="#f2661c" stroke-width="2"/></svg>
    </div>
    <div class="social-top"><span></span><span></span></div>

    <nav class="main-nav">
      <span class="has-menu">About Us</span><span>Features</span><span>FAQ</span><span>Blog</span><span>Press</span>
    </nav>
    <div class="account">Register / Login</div>
  </header>

  <section class="hero">
    <div class="hero-photo" role="img" aria-label="Concert crowd with raised hands under blue stage lights"></div>
    <div class="hero-crowd"></div>
    <h1 class="hero-title">PEACE OF MIND</h1>
    <p class="hero-lead">Welcome to Tarnalo we connect festivals and event<br>organizers with the people that make it happen</p>
    <div class="cta">Get Started</div>
  </section>

  <div class="menu menu-primary">
    <div class="menu-item">Link button simple 1<small>Special informations about link</small></div>
    <div class="menu-item">Drop-down menu Button 2</div>
    <div class="menu-item is-hover">Link button Rollover 3</div>
  </div>
  <div class="menu menu-sub">
    <div class="menu-item is-hover">Drop-down menu Button 2</div>
    <div class="menu-item">Link button Rollover 3</div>
  </div>

  <div class="slider-track"></div>
  <div class="slider-progress"></div>
  <div class="slider-dot is-active" style="left:403px"></div>
  <div class="slider-dot" style="left:493px"></div>
  <div class="slider-dot" style="left:587px"></div>
  <div class="slider-dot" style="left:680px"></div>
  <div class="slider-dot" style="left:771px"></div>
  <div class="slider-arrow" style="left:260px"><svg width="10" height="14" viewBox="0 0 10 14"><path d="M8 1 2 7l6 6" fill="#999"/></svg></div>
  <div class="slider-arrow" style="left:903px"><svg width="10" height="14" viewBox="0 0 10 14"><path d="M2 1l6 6-6 6" fill="#999"/></svg></div>

  <main>
    <article class="feature" style="left:218px;top:465px">
      <svg width="60" height="46" viewBox="0 0 60 46"><rect x="4" y="4" width="46" height="30" fill="#eee"/><rect x="10" y="12" width="32" height="22" rx="2" fill="none" stroke="#f2661c" stroke-width="3"/><path d="M20 40h12M26 34v6" stroke="#f2661c" stroke-width="3"/><rect x="40" y="20" width="12" height="20" rx="2" fill="#fff" stroke="#f2661c" stroke-width="2.5" transform="rotate(20 46 30)"/></svg>
      <h2 class="feature-title">Online Applications</h2>
      <p class="feature-text">Morbi purus orci, volutpat eget egestas eu, lacinia sed metus. Duis dignissim, ligula ut dapibus euismod.</p>
    </article>

    <article class="feature is-hover" style="left:491px;top:465px">
      <svg width="60" height="46" viewBox="0 0 60 46"><rect x="6" y="6" width="48" height="34" fill="#eee"/><rect x="14" y="9" width="32" height="30" rx="2" fill="none" stroke="#f2661c" stroke-width="3"/><line x1="14" y1="17" x2="46" y2="17" stroke="#f2661c" stroke-width="3"/><path d="M21 4v8M39 4v8" stroke="#f2661c" stroke-width="3"/><path d="M22 27l5 5 10-10" fill="none" stroke="#f2661c" stroke-width="3"/></svg>
      <h2 class="feature-title">Integrated Scheduling</h2>
      <p class="feature-text">Duis dignissim, ligula ut dapibus euismod.Morbi purus orci,</p>
      <div class="feature-more">Learn more</div>
      <div class="feature-corner"></div>
    </article>

    <article class="feature" style="left:764px;top:465px">
      <svg width="60" height="46" viewBox="0 0 60 46"><rect x="14" y="6" width="24" height="34" rx="2" fill="none" stroke="#f2661c" stroke-width="3"/><rect x="18" y="10" width="16" height="24" fill="#fde3d4"/><rect x="40" y="18" width="12" height="22" rx="2" fill="none" stroke="#f2661c" stroke-width="2.5"/></svg>
      <h2 class="feature-title">Native Phone and Tablet Apps</h2>
      <p class="feature-text">Morbi purus orci, volutpat eget egestas eu, lacinia sed metus. Duis dignissim, ligula ut dapibus euismod.</p>
    </article>

    <article class="feature" style="left:218px;top:696px">
      <svg width="60" height="46" viewBox="0 0 60 46"><rect x="6" y="6" width="40" height="32" fill="#eee"/><rect x="8" y="12" width="34" height="26" rx="1" fill="none" stroke="#f2661c" stroke-width="3"/><line x1="8" y1="18" x2="42" y2="18" stroke="#f2661c" stroke-width="2"/><path d="M13 33l7-7 5 4 9-9" fill="none" stroke="#f2661c" stroke-width="2.5"/><path d="M48 16a9 9 0 1 0 9 9h-9z" fill="#f2661c"/></svg>
      <h2 class="feature-title">Real-time Analystics</h2>
      <p class="feature-text">Duis eleifend bibendum risus, et accumsan orci lobortis eget. Nullam nec metus viverra, rutrum felis et, rhoncus</p>
    </article>

    <article class="feature" style="left:491px;top:696px">
      <svg width="60" height="46" viewBox="0 0 60 46"><path d="M4 14h16M2 22h14M4 30h16" stroke="#ddd" stroke-width="2.5"/><rect x="20" y="8" width="24" height="30" rx="2" fill="none" stroke="#f2661c" stroke-width="3"/><circle cx="31" cy="21" r="6" fill="none" stroke="#f2661c" stroke-width="2.5"/><line x1="35" y1="26" x2="40" y2="32" stroke="#f2661c" stroke-width="3"/><path d="M46 14h10M46 22h12" stroke="#ddd" stroke-width="2.5"/></svg>
      <h2 class="feature-title">Social Network Integration</h2>
      <p class="feature-text">Duis dignissim, ligula ut dapibus euismod.Morbi purus orci,</p>
    </article>

    <article class="feature" style="left:764px;top:696px">
      <svg width="70" height="46" viewBox="0 0 70 46"><rect x="8" y="14" width="22" height="14" rx="2" fill="none" stroke="#f2661c" stroke-width="2.5" transform="rotate(-20 19 21)"/><rect x="16" y="20" width="22" height="14" rx="2" fill="#fff" stroke="#f2661c" stroke-width="2.5" transform="rotate(10 27 27)"/><line x1="44" y1="6" x2="44" y2="40" stroke="#f2661c" stroke-width="3"/><path d="M44 7h20l-5 7 5 7H44z" fill="#f2661c"/></svg>
      <h2 class="feature-title">Enchanced Sponsorship Oppourunities</h2>
      <p class="feature-text">Cras eu eros varius, interdum eros sit amet, lacinia justo.</p>
    </article>
  </main>

  <footer>
    <div class="site-footer">
      <nav class="footer-nav"><span>About Us</span><span>Features</span><span>FAQ</span><span>Blog</span><span>Press</span></nav>
      <div class="footer-social">
        <span><i></i>Subscribe</span><span><i></i>Like Us</span><span><i></i>Follow Us</span><span><i></i>Join Us</span>
      </div>
      <div class="footer-brand"><i></i>TARNALO</div>
    </div>
    <div class="footer-base">
      <div class="copyright">© 2013 Tarnalo, a Plinth Framework. All Rights Reserved.</div>
      <div class="footer-links"><span>hello@tarnalo.com</span><span>Phone: (800) 555-0148</span><span>Privacy Policy</span><span>Terms and Conditions</span></div>
    </div>
  </footer>

</div>
</body>
</html>
```